Business Card Design Project - Photographer

Photography business needs a logo. I would like to see creative licence on options on 1 & 2 sided. I really like the concept of a fully / partially frosted design. I have already used ArtHive for my Logo, so I am looking for the same level of assistance with this project.

If you have any questions please let me know

Cheers Morris

Industry/Entity Type

Business

Requirements
Must have
• These are my contact details
Name: Morris Tilbury
Mobile: 0438 216 907
email: morris@brightlensstudio.com.au
Website: www.brightlensstudio.com.au
Nice to have
• Facebook: https://www.facebook.com/BrightLensStudioAus

```html
<!DOCTYPE html>
<html lang="en">
<head>
<meta charset="utf-8">
<title>Bright Lens Studio – Business Card</title>
<link href="https://fonts.googleapis.com/css2?family=Source+Sans+3:wght@400;600;700&display=swap" rel="stylesheet">
<style>
  :root {
    --page-bg: #efece7;
    --frost-top: #d9d5ce;
    --frost-bottom: #bdb7ae;
    --brand-red: #d2232a;
    --ink: #262626;
    --photo-light: #c9c0ad;
    --photo-mid: #8f8a6e;
    --photo-dark: #4f5a3f;
  }
  * { margin: 0; padding: 0; box-sizing: border-box; }
  html, body {
    width: 1200px;
    height: 800px;
    overflow: hidden;
    background: var(--page-bg);
    font-family: "Source Sans 3", "Myriad Pro", Arial, sans-serif;
  }
  .canvas {
    width: 1200px;
    height: 800px;
    display: flex;
    align-items: center;
    justify-content: center;
  }
  .card {
    position: relative;
    width: 1000px;
    height: 560px;
    border-radius: 30px;
    overflow: hidden;
    background: linear-gradient(160deg, var(--frost-top), var(--frost-bottom));
    box-shadow: 0 18px 40px rgba(0,0,0,0.18);
  }
  .card__photo {
    position: absolute;
    left: 0;
    top: 0;
    width: 410px;
    height: 560px;
    border-top-right-radius: 34px;
    border-bottom-right-radius: 34px;
    background:
      radial-gradient(ellipse at 55% 45%, var(--photo-light) 0%, transparent 55%),
      linear-gradient(160deg, var(--photo-dark) 0%, var(--photo-mid) 45%, var(--photo-light) 100%);
  }
  .card__info {
    position: absolute;
    left: 470px;
    top: 70px;
    right: 30px;
    color: var(--ink);
  }
  .brand {
    display: flex;
    align-items: center;
    gap: 14px;
    margin-left: 20px;
    margin-bottom: 44px;
    white-space: nowrap;
  }
  .brand__mark {
    width: 38px;
    height: 38px;
    flex: none;
    background: var(--brand-red);
  }
  .brand__name {
    font-weight: 700;
    font-size: 36px;
    letter-spacing: 1px;
    color: var(--brand-red);
    text-transform: uppercase;
    line-height: 1;
  }
  .person {
    font-weight: 700;
    font-size: 50px;
    line-height: 1;
    margin-bottom: 30px;
  }
  .person__first { color: var(--brand-red); }
  .person__last { color: var(--ink); }
  .contacts { list-style: none; }
  .contact {
    display: flex;
    align-items: center;
    gap: 10px;
    font-size: 27px;
    font-weight: 600;
    line-height: 1.55;
    white-space: nowrap;
  }
  .contact__icon {
    width: 24px;
    height: 24px;
    flex: none;
  }
  .contact__icon path,
  .contact__icon circle,
  .contact__icon rect { fill: var(--brand-red); }
  .contact__icon .stroke { fill: none; stroke: var(--brand-red); stroke-width: 2; }
  .contact__icon .envelope-flap { fill: none; stroke: var(--frost-top); stroke-width: 1.6; }
  .social {
    font-size: 27px;
    font-weight: 600;
    line-height: 1.45;
    margin-top: 10px;
    white-space: nowrap;
  }
  .social__site { color: var(--brand-red); }
</style>
</head>
<body>
<main class="canvas">
  <article class="card">
    <div class="card__photo" role="img" aria-label="Portrait photograph of a young child in a cap sitting outdoors"></div>

    <section class="card__info">
      <div class="brand">
        <span class="brand__mark"></span>
        <span class="brand__name">Bright Lens Studio</span>
      </div>

      <h1 class="person">
        <span class="person__first">Morris</span>
        <span class="person__last">Tilbury</span>
      </h1>

      <ul class="contacts">
        <li class="contact">
          <svg class="contact__icon" viewBox="0 0 24 24" aria-hidden="true">
            <path d="M6.6 10.8c1.4 2.8 3.8 5.2 6.6 6.6l2.2-2.2c.3-.3.7-.4 1-.2 1.1.4 2.3.6 3.6.6.6 0 1 .4 1 1V20c0 .6-.4 1-1 1C10.6 21 3 13.4 3 4c0-.6.4-1 1-1h3.5c.6 0 1 .4 1 1 0 1.3.2 2.5.6 3.6.1.3 0 .7-.2 1l-2.3 2.2z"/>
          </svg>
          <span>: 0438 216 907</span>
        </li>
        <li class="contact">
          <svg class="contact__icon" viewBox="0 0 24 24" aria-hidden="true">
            <rect x="2" y="5" width="20" height="14" rx="1"/>
            <path class="envelope-flap" d="M2 6l10 7 10-7"/>
          </svg>
          <span>: morris@brightlensstudio.com.au</span>
        </li>
        <li class="contact">
          <svg class="contact__icon" viewBox="0 0 24 24" aria-hidden="true">
            <circle class="stroke" cx="12" cy="12" r="9"/>
            <path class="stroke" d="M3 12h18M12 3c3 3 3 15 0 18M12 3c-3 3-3 15 0 18"/>
          </svg>
          <span>: www.brightlensstudio.com.au</span>
        </li>
      </ul>

      <p class="social"><span class="social__site">socialhub.net/</span>BrightLensStudioAus</p>
    </section>
  </article>
</main>
</body>
</html>
```